business card for trucking industry consulting firm

Our company, Velmora Services Inc. provides numerous services to the trucking industry as listed on our website: velmora.ca
The logo i want on the card is the black and red VELMORA
update: i would like the services we provide listed on the card (see velmora.ca)

```html
<!DOCTYPE html>
<html lang="en">
<head>
<meta charset="utf-8">
<title>Velmora Services Inc. – Business Card</title>
<link rel="stylesheet" href="https://fonts.googleapis.com/css2?family=Arimo:wght@400;700&display=swap">
<style>
  :root {
    --backdrop: #5c5c5e;
    --ink-dark: #160608;
    --accent-red: #d8232a;
    --paper: #f3f3f1;
    --text-light: #ffffff;
    --text-dark: #1d1d1d;
  }
  * { margin: 0; padding: 0; box-sizing: border-box; }
  html, body {
    width: 1200px; height: 800px; overflow: hidden;
    background: var(--backdrop);
    font-family: "Arimo", Arial, sans-serif;
  }
  .canvas { position: relative; width: 1200px; height: 800px; }
  .card {
    position: absolute; top: 102px;
    width: 340px; height: 595px;
    background: var(--paper);
    overflow: hidden;
  }
  .card--back { left: 190px; }
  .card--front { left: 670px; }
  .card-shapes { position: absolute; inset: 0; }

  /* Back */
  .website {
    position: absolute; left: 105px; top: 70px;
    color: var(--text-light); font-size: 15px; letter-spacing: .2px;
  }
  .services { position: absolute; left: 58px; top: 245px; }
  .services-title { color: var(--accent-red); font-size: 13px; margin-bottom: 8px; }
  .services-list { list-style: none; }
  .services-list li {
    position: relative; padding-left: 14px;
    font-size: 11.5px; line-height: 19px; color: var(--text-dark);
  }
  .services-list li::before {
    content: ""; position: absolute; left: 0; top: 7px;
    width: 5px; height: 5px; border-radius: 50%;
    background: var(--accent-red);
  }

  /* Front */
  .wordmark {
    position: absolute; right: 34px; top: 34px; text-align: right;
    color: var(--ink-dark); font-weight: 700; line-height: 1;
  }
  .wordmark-name { font-size: 34px; letter-spacing: .5px; }
  .wordmark-sub { font-size: 12px; letter-spacing: 2px; margin-top: 4px; }
  .person { position: absolute; left: 62px; top: 228px; color: var(--text-light); }
  .person-name { font-size: 28px; font-weight: 400; letter-spacing: .5px; }
  .person-title { font-size: 11.5px; margin-top: 4px; }
  .contact { position: absolute; left: 90px; color: var(--text-light); font-size: 13px; line-height: 17px; }
  .contact--address { top: 316px; }
  .contact--phone { top: 392px; }
  .contact--email { top: 466px; }
</style>
</head>
<body>
<main class="canvas">

  <section class="card card--back" aria-label="Business card back">
    <svg class="card-shapes" width="340" height="595" viewBox="0 0 340 595">
      <polygon points="0,0 340,0 340,125 165,215 0,115" fill="var(--ink-dark)"/>
      <polyline points="0,115 165,215 340,125" fill="none" stroke="var(--accent-red)" stroke-width="3"/>
      <polygon points="0,470 0,595 190,595" fill="var(--ink-dark)"/>
      <line x1="0" y1="470" x2="190" y2="595" stroke="var(--accent-red)" stroke-width="3"/>
    </svg>
    <p class="website">www.velmora.co</p>
    <div class="services">
      <h2 class="services-title">Our Services</h2>
      <ul class="services-list">
        <li>Prorate Licensing</li>
        <li>Safety Fitness Certificates (SFC)</li>
        <li>Compliance and Audit Assistance</li>
        <li>IFTA Fuel Tax Reporting</li>
        <li>Log Book Auditing</li>
        <li>Travel to USA</li>
        <li>Written Safety &amp; Maintenance Programs</li>
      </ul>
    </div>
  </section>

  <section class="card card--front" aria-label="Business card front">
    <svg class="card-shapes" width="340" height="595" viewBox="0 0 340 595">
      <polygon points="0,170 170,110 340,170 340,595 0,595" fill="var(--ink-dark)"/>
      <polyline points="0,170 170,110 340,170" fill="none" stroke="var(--accent-red)" stroke-width="3"/>
      <g fill="none" stroke="var(--text-light)" stroke-width="2">
        <line x1="55" y1="344" x2="55" y2="384"/>
        <line x1="55" y1="420" x2="55" y2="458"/>
        <polygon points="55,308 72,317 72,335 55,344 38,335 38,317"/>
        <polygon points="55,384 72,393 72,411 55,420 38,411 38,393"/>
        <polygon points="55,458 72,467 72,485 55,494 38,485 38,467"/>
      </g>
      <g fill="var(--text-light)">
        <path d="M55,334 C50,328 48,325 48,322 a7,7 0 0 1 14,0 c0,3 -2,6 -7,12z"/>
        <circle cx="55" cy="322" r="2.4" fill="var(--ink-dark)"/>
        <path d="M49,396 c1,-2 3,-3 4,-2 l2,3 c0,1 -1,2 -2,2 c1,3 3,5 6,6 c0,-1 1,-2 2,-2 l3,2 c1,1 0,3 -2,4 c-6,0 -13,-7 -13,-13z"/>
        <rect x="47" y="470" width="16" height="12"/>
      </g>
      <polyline points="47,470 55,477 63,470" fill="none" stroke="var(--ink-dark)" stroke-width="1.5"/>
    </svg>
    <div class="wordmark">
      <p class="wordmark-name">VELMORA</p>
      <p class="wordmark-sub">Services Inc.</p>
    </div>
    <div class="person">
      <h1 class="person-name">Dana Kerr</h1>
      <p class="person-title">Chief Executive Officer</p>
    </div>
    <p class="contact contact--address">#305, 8840-52 Ave<br>Edmonton, Alberta T6B 4K8<br>Canada</p>
    <p class="contact contact--phone">1-800-VELMORA (835-6672)<br>780-555-0148</p>
    <p class="contact contact--email">admin@velmora.ca</p>
  </section>

</main>
</body>
</html>
```